New Business Card Design Project

2 sided business card required. I have attached some previous designs of items we have had made so you can see the logo etc. we Want the card to look professional and modern. for the final design upload for winning designer please note I need to be able to edit the names / phone numbers on the card design as I need to get them made for different staff.
Updates

extending time so designers can have time to submit

Target Market(s)

new customers

Industry/Entity Type

transport / earthmoving

Contact Information for Business Card

name, phone number email address

Requirements
Nice to have
• professional / impressive looking card (first impressions to customers count)
Should not have
• do not put our mobile number on the design use a generic number

```html
<!DOCTYPE html>
<html lang="en">
<head>
<meta charset="utf-8">
<title>KRD Pty Ltd – Business Card</title>
<link rel="stylesheet" href="https://fonts.googleapis.com/css2?family=Exo+2:wght@300;400;600;700&family=Montserrat:wght@700;800&display=swap">
<style>
  :root {
    --page: #e9e6e1;
    --card: #1f1f21;
    --card-deep: #161618;
    --facet: #2b2b2e;
    --facet-light: #333337;
    --silver: #a9abae;
    --white: #ffffff;
    --orange: #e0a24a;
    --muted: #8d8d90;
    --sand: #b98a5a;
    --sand-light: #d8b48a;
  }
  * { margin: 0; padding: 0; box-sizing: border-box; }
  html, body { width: 1200px; height: 900px; overflow: hidden; }
  body {
    background: var(--page);
    font-family: "Exo 2", "Segoe UI", sans-serif;
    position: relative;
  }
  .card {
    position: absolute;
    left: 260px;
    width: 680px;
    height: 388px;
    background: var(--card);
    border-radius: 4px;
    overflow: hidden;
    box-shadow: 0 6px 18px rgba(0,0,0,.18);
  }
  .card--front { top: 50px; }
  .card--back { top: 462px; }

  .facets { position: absolute; inset: 0; }

  .brand {
    position: absolute;
    display: flex;
    align-items: baseline;
    gap: 10px;
    color: var(--silver);
    font-family: "Exo 2", sans-serif;
    font-weight: 700;
  }
  .brand__name { letter-spacing: 2px; }
  .brand__suffix { font-weight: 700; }

  .card--front .brand { left: 44px; top: 34px; }
  .card--front .brand__name { font-size: 54px; line-height: 1; }
  .card--front .brand__suffix { font-size: 14px; }

  .person { position: absolute; left: 250px; top: 92px; }
  .person__name {
    font-family: "Montserrat", sans-serif;
    font-weight: 800;
    font-size: 34px;
    color: var(--white);
    line-height: 1.1;
  }
  .person__role {
    font-size: 16px;
    color: var(--orange);
    margin-left: 90px;
  }

  .contact {
    position: absolute;
    left: 44px;
    bottom: 40px;
    list-style: none;
    color: var(--white);
    font-size: 19px;
    line-height: 1.15;
  }
  .contact li { display: flex; align-items: flex-start; gap: 8px; }
  .contact svg { flex: none; margin-top: 3px; }
  .contact__indent { padding-left: 24px; }

  .services {
    position: absolute;
    left: 26px;
    right: 26px;
    top: 20px;
    color: var(--muted);
    font-size: 12.5px;
    line-height: 1.3;
    letter-spacing: .2px;
  }
  .services__title { text-transform: uppercase; }
  .rule {
    position: absolute;
    left: 0; right: 0; top: 104px;
    height: 1px;
    background: #3a3a3d;
  }
  .card--back .brand { left: 230px; top: 150px; }
  .card--back .brand__name { font-size: 66px; line-height: 1; }
  .card--back .brand__suffix { font-size: 18px; }

  .photo {
    position: absolute;
    left: 0; right: 0; bottom: 0;
    height: 170px;
    background: linear-gradient(180deg, rgba(31,31,33,0) 0%, #5a4636 30%, var(--sand) 60%, var(--sand-light) 100%);
  }
</style>
</head>
<body>

<section class="card card--front" aria-label="Business card front">
  <svg class="facets" width="680" height="388" viewBox="0 0 680 388" aria-hidden="true">
    <polygon points="0,70 680,20 680,190 120,235" fill="var(--facet)"/>
    <polygon points="400,0 680,0 680,210 560,260" fill="var(--facet-light)" opacity=".6"/>
    <polygon points="0,235 680,190 680,388 0,388" fill="var(--card-deep)"/>
  </svg>

  <div class="brand">
    <span class="brand__name">KRD</span>
    <span class="brand__suffix">Pty Ltd</span>
  </div>

  <div class="person">
    <p class="person__name">Your Name</p>
    <p class="person__role">Manager</p>
  </div>

  <ul class="contact">
    <li>
      <svg width="16" height="16" viewBox="0 0 16 16" aria-hidden="true"><circle cx="8" cy="8" r="7" fill="none" stroke="var(--orange)" stroke-width="1.5"/><path d="M8 4a2.5 2.5 0 0 0-2.5 2.5C5.5 9 8 12 8 12s2.5-3 2.5-5.5A2.5 2.5 0 0 0 8 4z" fill="var(--orange)"/></svg>
      <span>Lot 41 9 Mile Road</span>
    </li>
    <li class="contact__indent">Redstone Flat</li>
    <li>
      <svg width="16" height="16" viewBox="0 0 16 16" aria-hidden="true"><circle cx="8" cy="8" r="7" fill="none" stroke="var(--orange)" stroke-width="1.5"/><rect x="4.5" y="5.5" width="7" height="5" fill="none" stroke="var(--orange)" stroke-width="1.2"/><path d="M4.5 5.5 8 8.5l3.5-3" fill="none" stroke="var(--orange)" stroke-width="1.2"/></svg>
      <span>yourname@KRDPTYLTD.com</span>
    </li>
    <li>
      <svg width="16" height="16" viewBox="0 0 16 16" aria-hidden="true"><circle cx="8" cy="8" r="7" fill="none" stroke="var(--orange)" stroke-width="1.5"/><path d="M5.5 4.5l1.5 0 .7 1.8-1 .8a5 5 0 0 0 2.2 2.2l.8-1 1.8.7 0 1.5c-3.5.3-6.3-2.5-6-6z" fill="var(--orange)"/></svg>
      <span>100 5550199</span>
    </li>
  </ul>
</section>

<section class="card card--back" aria-label="Business card back">
  <div class="services">
    <p class="services__title">Services offered:</p>
    <p>Oversize Loads / Hot Shot Loads . Heavy Vehicle Recovery Services . Potable Water Deliveries . Road Building/Maintenance . Earthworks . Sand &amp; Metal Supply &amp; Cartage . Road Train Tippers . Road Train Tankers . Road Train Flat Tops . Drop Deck Trailers</p>
  </div>
  <div class="rule"></div>

  <div class="photo" role="img" aria-label="Photo of a black road train truck with three tipper trailers on a red dirt outback track"></div>

  <div class="brand">
    <span class="brand__name">KRD</span>
    <span class="brand__suffix">Pty Ltd</span>
  </div>
</section>

</body>
</html>
```